Business Card Design Project

Business card based on attached logo

Tom Pellis
Tom@vorlatests.example
555-014-7731 ext. 219
Www.VorlaTests.example

Industry/Entity Type

Business

```html
<!DOCTYPE html>
<html lang="en">
<head>
<meta charset="utf-8">
<title>Vorla Tests Business Card – Front &amp; Back</title>
<link rel="stylesheet" href="https://fonts.googleapis.com/css2?family=Open+Sans:wght@400;600;700&display=swap">
<style>
  :root {
    --canvas: #8f9091;
    --card-white: #ffffff;
    --card-grey: #e6e6e6;
    --plate-grey: #e3e3e3;
    --brand-red: #ed1c24;
    --brand-black: #231f20;
    --ink: #3a3a3a;
  }
  * { box-sizing: border-box; margin: 0; padding: 0; }
  html, body { width: 1200px; height: 1000px; overflow: hidden; }
  body {
    background: var(--canvas);
    font-family: "Open Sans", Arial, sans-serif;
    position: relative;
  }
  .card {
    position: absolute;
    left: 250px;
    width: 700px;
    height: 400px;
    box-shadow: 0 6px 18px rgba(0,0,0,.25);
    overflow: hidden;
  }
  /* Back panel */
  .card--back { top: 70px; background: var(--card-white); }
  .logo-plate {
    position: absolute;
    left: 225px; top: 120px;
    width: 250px; height: 90px;
    background: var(--plate-grey);
    box-shadow: 4px 6px 8px rgba(0,0,0,.35);
    display: flex; align-items: center; justify-content: center;
  }
  .wordmark {
    font-weight: 700;
    color: var(--brand-black);
    text-align: center;
    line-height: 1;
    letter-spacing: .04em;
  }
  .logo-plate .wordmark { font-size: 30px; }
  .back-url {
    position: absolute;
    left: 0; right: 0; top: 290px;
    text-align: center;
    font-size: 17px;
    color: var(--brand-black);
    letter-spacing: .02em;
  }
  /* Front panel */
  .card--front { top: 530px; background: var(--card-grey); }
  .contact {
    position: absolute;
    left: 28px; top: 26px;
    font-size: 15px;
    line-height: 1.45;
    color: var(--ink);
  }
  .band { position: absolute; }
  .band--red { left: 0; top: 110px; width: 330px; height: 80px; background: var(--brand-red); }
  .band--black { left: 330px; top: 190px; width: 370px; height: 80px; background: var(--brand-black); }
  .logo-disc {
    position: absolute;
    left: 240px; top: 100px;
    width: 180px; height: 180px;
    border-radius: 50%;
    background: var(--card-white);
    display: flex; align-items: center; justify-content: center;
  }
  .logo-disc .wordmark { font-size: 32px; }
  .holder-name {
    position: absolute;
    right: 28px; top: 140px;
    display: flex; align-items: center; gap: 8px;
    font-size: 17px; font-weight: 700;
    color: var(--brand-black);
  }
  .holder-name .mark-square {
    width: 12px; height: 12px; background: var(--brand-red);
  }
</style>
</head>
<body>
  <section class="card card--back" aria-label="Business card back">
    <div class="logo-plate"><p class="wordmark">VORLA<br>TESTS</p></div>
    <p class="back-url">www.vorlatests.example</p>
  </section>

  <section class="card card--front" aria-label="Business card front">
    <div class="contact">
      <p>1-555-014-7731 ext 219</p>
      <p>Tom@vorlatests.example</p>
    </div>
    <div class="band band--red"></div>
    <div class="band band--black"></div>
    <div class="logo-disc"><p class="wordmark">VORLA<br>TESTS</p></div>
    <p class="holder-name">Tom Pellis <span class="mark-square"></span></p>
  </section>
</body>
</html>
```